Aviation security consulting company needs a website

We need a website design for Brisk Holloway, and aviation security consulting company. Brisk Holloway (www.briskholloway.example) is an aviation security consulting company that works with government and industry stakeholders in over 60 countries on aviation security strategy, governance, and oversight at the regulatory and operational level.
Brisk Holloway is strongly internationally focused.
The website required should be simple, corporate, serious, and communicate professionalism, reliability and honesty. We are trying to give the company a feeling of being well established.
The attached files include the company logo, along with examples of company web page styles that we like.
The Brisk Holloway website need only be around five pages long (landing page, who we are, our services, our clients, contact), though don't feel limited to only five pages.
The existing website (www.briskholloway.example) was rushed and put together using Wix. We don't love the existing website as it looks too amateur, so don't use it as a template.
There is no requirement for any online sales tools to be included in the site. The site is purely informational, with the option of people making contact via email.

```html
<!DOCTYPE html>
<html lang="en">
<head>
<meta charset="utf-8">
<title>Brisk Holloway — Aviation Security Consulting</title>
<link href="https://fonts.googleapis.com/css2?family=Montserrat:wght@700;800&family=Open+Sans:wght@400;600;700&display=swap" rel="stylesheet">
<style>
:root{
  --ink:#333;
  --muted:#777;
  --soft:#999;
  --accent:#c0392b;
  --navy:#1d2a5a;
  --panel:#f8f8f8;
  --line:#e4e4e4;
  --dark:#333333;
  --footer:#222222;
  --footer-bar:#2c2c2c;
  --white:#fff;
}
*{box-sizing:border-box;margin:0;padding:0}
html,body{width:1200px;height:1200px;overflow:hidden;background:var(--white)}
body{font-family:"Open Sans",Arial,sans-serif;color:var(--ink)}
.stage{position:absolute;left:0;top:0;width:1500px;height:1500px;transform:scale(.8);transform-origin:0 0}
.abs{position:absolute}
a{color:var(--accent);text-decoration:none}

/* header */
.brand{left:499px;top:1px;display:flex;align-items:center;gap:5px}
.brand-mark{width:22px;height:22px;background:var(--navy)}
.brand-name{font-size:13px;font-weight:600;color:var(--navy);line-height:14px}
.brand-tag{font-size:5.5px;color:var(--navy);letter-spacing:.8px;line-height:7px}
.nav{left:678px;top:8px;display:flex;gap:11px;font-size:6.5px;color:var(--muted)}
.nav .on{color:var(--ink);font-weight:600}

/* hero */
.hero{left:306px;top:30px;width:884px;height:222px;
  background:linear-gradient(180deg,#1f2d45 0%,#4a5f7c 30%,#9aa7b3 52%,#e0a060 72%,#e8641e 84%,#6d4a3a 100%)}
.hero h1{position:absolute;left:206px;top:86px;font-family:Montserrat,sans-serif;font-weight:800;
  font-size:29px;line-height:32px;color:var(--white);text-shadow:0 1px 3px rgba(0,0,0,.3)}

/* features */
.feature{top:273px;width:145px}
.feature h3{font-size:7.5px;letter-spacing:.8px;font-weight:600;display:flex;align-items:center;gap:5px;margin-bottom:8px}
.feature p{font-size:6px;line-height:10px;color:var(--muted)}

/* sections */
.rule{height:1px;background:var(--line);left:306px;width:884px}
.band{left:306px;width:884px}
.section-title{left:306px;width:884px;text-align:center;font-size:13px;letter-spacing:1px;font-weight:600}
.divider{left:672px;width:152px;height:1px;background:var(--line)}
.divider::after{content:"";position:absolute;left:73px;top:-2px;width:4px;height:4px;border:1px solid var(--line);border-radius:50%;background:var(--panel)}
.lead{left:306px;width:884px;text-align:center;font-size:6px;line-height:9.5px;color:var(--muted)}

.card{top:486px;width:159px;height:154px;background:var(--white);border:1px solid #eee}
.card .photo{height:128px}
.card p{font-size:6px;color:var(--muted);padding:7px 8px}

/* testimonials */
.quote{width:190px}
.quote .avatar{position:absolute;width:36px;height:36px;border-radius:50%}
.quote .body{position:absolute;left:46px;width:176px;font-size:6px;line-height:10px;color:var(--muted)}
.quote .who{font-weight:600;color:var(--ink);margin-top:4px}

/* help */
.help-title{color:var(--white)}
.help-card{top:1093px;width:141px;height:87px;background:var(--white);text-align:center;padding:21px 10px 0}
.help-card .badge{position:absolute;left:59px;top:-11px;width:23px;height:23px;border-radius:50%;background:var(--accent);
  display:flex;align-items:center;justify-content:center}
.help-card h4{font-size:7.5px;letter-spacing:.7px;font-weight:600;margin-bottom:7px}
.help-card p{font-size:6px;line-height:10px;color:var(--muted)}

/* partners */
.partners{left:496px;top:1214px;width:500px;display:flex;justify-content:space-between;align-items:center}
.partner{display:flex;align-items:center;gap:4px;font-size:11px;font-weight:700;color:#d71920}
.partner i{width:12px;height:12px;border-radius:50%;background:#d71920;display:block}

/* footer */
.footer{left:306px;top:1251px;width:884px;height:216px;background:var(--footer)}
.fcol{top:1278px;width:120px;font-size:6px;line-height:10px;color:#ddd}
.fcol h5{font-size:6.5px;letter-spacing:.8px;color:#aaa;font-weight:600;margin-bottom:6px}
.news{display:flex;gap:6px;margin-bottom:6px}
.news .thumb{width:14px;height:14px;background:#8a6a5a;flex:none}
.news small{display:block;color:#888;font-size:5px}
.tags{display:flex;flex-wrap:wrap;gap:3px;width:100px}
.tags span{border:1px solid #444;padding:0 3px;font-size:5px;line-height:9px}
.social{display:flex;gap:14px;margin-top:22px}
.social div{display:flex;gap:3px;align-items:center;font-size:5px;line-height:6px}
.social b{width:13px;height:13px;display:block}
.bar{left:306px;top:1467px;width:884px;height:23px;background:var(--footer-bar);font-size:5.5px;color:#ccc}
.bar .copy{position:absolute;left:203px;top:8px}
.bar .links{position:absolute;left:435px;top:8px;display:flex;gap:9px}
</style>
</head>
<body>
<div class="stage">

  <header>
    <div class="abs brand">
      <span class="brand-mark"></span>
      <div><div class="brand-name">Brisk Holloway</div><div class="brand-tag">aviation security consulting</div></div>
    </div>
    <nav class="abs nav">
      <span class="on">Home</span><span>Regulators</span><span>Capacity Development</span><span>Airports</span><span>Airlines</span><span>Air Cargo</span><span>Contact Us</span>
      <svg width="8" height="8" viewBox="0 0 8 8"><circle cx="3.2" cy="3.2" r="2.3" fill="none" stroke="#777"/><path d="M5 5l2.5 2.5" stroke="#777"/></svg>
    </nav>
  </header>

  <section class="abs hero" role="img" aria-label="Sunset sky above the clouds seen past an aircraft wing">
    <h1>When you need<br>expert air consultation.</h1>
  </section>

  <section>
    <div class="abs feature" style="left:509px">
      <h3><svg width="9" height="9" viewBox="0 0 10 10"><circle cx="5" cy="5" r="4" fill="none" stroke="#333" stroke-width="1.2"/><path d="M5 2.5V5h2" stroke="#333" fill="none"/></svg>OUR HERITAGE</h3>
      <p>We have been helping airlines in securities since 1995 and over the years we have helped them.</p>
    </div>
    <div class="abs feature" style="left:678px">
      <h3><svg width="9" height="9" viewBox="0 0 10 10"><circle cx="5" cy="5" r="4" fill="none" stroke="#333" stroke-width="1.2"/><circle cx="5" cy="5" r="1.6" fill="none" stroke="#333"/></svg>ON THE CLOCK SUPPORT</h3>
      <p>135.000 customers cant be wrong. We have our support team on standby if you need help.</p>
    </div>
    <div class="abs feature" style="left:847px">
      <h3><svg width="9" height="9" viewBox="0 0 10 10"><path d="M9 1L3 4l3 3zM3 7l-2 2" stroke="#333" fill="#333"/></svg>WORLD CLASS HELP</h3>
      <p>Our enginners are highly trained in <a>all skill levels</a> without problems</p>
    </div>
  </section>

  <div class="abs rule" style="top:344px"></div>
  <section class="abs band" style="top:345px;height:378px;background:var(--panel)"></section>
  <h2 class="abs section-title" style="top:376px">AVIATION SECURITY YOU CAN TRUST</h2>
  <div class="abs divider" style="top:409px"></div>
  <p class="abs lead" style="top:429px">We offer world class <a style="font-weight:600">advice and</a> help to all our customers.<br>We work with government and industry on aviation security regulatory and operational strategy, governance, and oversight.</p>

  <div class="abs card" style="left:509px"><div class="photo" role="img" aria-label="Airline pilot in uniform beside a jet" style="background:linear-gradient(135deg,#cfd7df,#8b97a3)"></div><p>Flight Safety</p></div>
  <div class="abs card" style="left:668px"><div class="photo" role="img" aria-label="Engineer in hard hat reviewing plans" style="background:linear-gradient(135deg,#e8893a,#e9edf1 55%)"></div><p>Aerospace Understanding</p></div>
  <div class="abs card" style="left:827px"><div class="photo" role="img" aria-label="Aerial view of airport terminal and parked aircraft" style="background:linear-gradient(180deg,#9aa5ad,#6f7679)"></div><p>Support Team</p></div>

  <div class="abs divider" style="top:658px"></div>
  <a class="abs" style="left:733px;top:677px;font-size:6px">Contact Us</a>

  <div class="abs rule" style="top:723px"></div>
  <h2 class="abs section-title" style="top:756px">WHAT OUR CUSTOMERS SAY ABOUT US</h2>
  <div class="abs divider" style="top:789px;"></div>

  <div class="abs" style="left:748px;top:812px;width:1px;height:150px;background:var(--line)"></div>
  <div class="abs" style="left:509px;top:891px;width:478px;height:1px;background:var(--line)"></div>

  <div class="abs quote" style="left:518px;top:818px">
    <div class="avatar" role="img" aria-label="Portrait of customer" style="background:#b89478"></div>
    <div class="body" style="top:0">Nulla consequat massa quis enim. Donec pede justo, fringilla vel, aliquet nec, vulputate eget, arcu. In enim justo, rhoncus ut, imperdiet a, venenatis vitae, justo. Nullam dictum felis eu pede mollis pretium. Integer tincidunt. Cras dapibus.
      <div class="who">Clara B. Hollis</div><div>Marketing – <a>RouteAtlas</a></div></div>
  </div>
  <div class="abs quote" style="left:758px;top:818px">
    <div class="avatar" role="img" aria-label="Portrait of customer" style="background:#a9806a"></div>
    <div class="body" style="top:0">In enim justo, rhoncus ut, imperdiet a, venenatis vitae, justo. Nullam dictum felis eu pede mollis pretium. Integer tincidunt. Cras dapibus.
      <div class="who">Ines Marlow</div><div>CEO – <a>Papertrail</a></div></div>
  </div>
  <div class="abs quote" style="left:518px;top:901px">
    <div class="avatar" role="img" aria-label="Portrait of customer" style="background:#7d6a5c"></div>
    <div class="body" style="top:0">Nulla consequat massa quis enim. Donec pede justo, fringilla vel, aliquet nec, vulputate eget, arcu.
      <div class="who">Otto Brandt</div><div>Public Relations – <a>Signalhouse</a></div></div>
  </div>
  <div class="abs quote" style="left:758px;top:901px">
    <div class="avatar" role="img" aria-label="Portrait of customer" style="background:#4b3a32"></div>
    <div class="body" style="top:0">In enim justo, rhoncus ut, imperdiet a, venenatis vitae, justo. Nullam dictum felis eu pede mollis pretium. Integer tincidunt. Cras dapibus.
      <div class="who">Dr. Quell</div><div>Dean of Medicine – <a>Harrow Inc</a></div></div>
  </div>

  <section class="abs band" style="top:1012px;height:191px;background:var(--dark)"></section>
  <h2 class="abs section-title help-title" style="top:1034px">IN CASE YOU NEED HELP</h2>
  <p class="abs lead" style="top:1056px;color:#eee">Here are several ways to contact us</p>

  <div class="abs help-card" style="left:509px">
    <span class="badge"><svg width="9" height="9" viewBox="0 0 10 10"><text x="5" y="8.5" text-anchor="middle" font-size="9" fill="#fff" font-family="Open Sans,sans-serif">?</text></svg></span>
    <h4>PRESALES QUESTION?</h4><p>Lorem ipsum dolor sit amet, consectetuer adipiscing elit. Aenean commodo ligula eget dolor. Aenean massa.<br><a>Learn more</a></p>
  </div>
  <div class="abs help-card" style="left:678px">
    <span class="badge"><svg width="10" height="10" viewBox="0 0 10 10"><circle cx="5" cy="5" r="3.6" fill="none" stroke="#fff" stroke-width="1.2"/><path d="M5 1.4v7.2M1.4 5h7.2" stroke="#fff"/></svg></span>
    <h4>NEED SUPPORT?</h4><p>Donec quam felis, ultricies nec, pellentesque eu, pretium quis, sem. Nulla consequat massa quis enim.<br><a>Learn more</a></p>
  </div>
  <div class="abs help-card" style="left:847px">
    <span class="badge"><svg width="9" height="9" viewBox="0 0 10 10"><rect x="2" y="1" width="6" height="8" fill="none" stroke="#fff"/><path d="M3.5 3.5h3M3.5 5h3M3.5 6.5h3" stroke="#fff" stroke-width=".7"/></svg></span>
    <h4>CHECK FORUM</h4><p>Donec pede justo, fringilla vel, aliquet nec, vulputate eget, arcu. In enim jusordiet a, venenatis vitae, justo.<br><a>Learn more</a></p>
  </div>

  <div class="abs partners">
    <span class="partner"><i></i>Kestrel Air</span>
    <span class="partner">Northwind</span>
    <span class="partner">Solace Airways</span>
    <span class="partner"><i></i>Meridian</span>
    <span class="partner">Tasman Air</span>
  </div>

  <footer>
    <div class="abs footer"></div>
    <div class="abs fcol" style="left:509px">
      <h5>INTERESTING LINKS</h5>
      <p>Check our our Linkbook page</p>
      <div class="social">
        <div><b style="background:#3aa3dc"></b>Follow<br>on Chatter</div>
        <div><b style="background:#f08a24"></b>Subscribe<br>to RSS Feed</div>
      </div>
    </div>
    <div class="abs fcol" style="left:636px">
      <h5>LATEST NEWS</h5>
      <div class="news"><span class="thumb"></span><div>Postformat Gallery: Multiple images<small>October 21, 2013 - 3:31 pm</small></div></div>
      <div class="news"><span class="thumb" style="background:#5c7080"></span><div>Snowboarding is fun!<small>December 12, 2012 - 9:11 pm</small></div></div>
      <div class="news"><span class="thumb" style="background:#c9a26a"></span><div>This is a standard post format with preview Picture<small>January 14, 2012 - 1:13 pm</small></div></div>
    </div>
    <div class="abs fcol" style="left:763px">
      <h5>TAGS</h5>
      <div class="tags"><span>are</span><span>econ</span><span>landscape</span><span>lifestyle</span><span>nice</span><span>portrait</span><span>some</span><span>tags</span><span>these</span></div>
      <h5 style="margin-top:18px">CATEGORIES</h5>
      <p>Breaking News<br>Economy<br>Frontpage Article<br>Health<br>Lifestyle<br>Music<br>News<br>Science</p>
    </div>
    <div class="abs fcol" style="left:889px;width:110px">
      <h5>BUSINESS HOURS</h5>
      <p>Our support Hotline is available 24 Hours a day: (555) 210 884 3302</p>
      <p style="margin-top:5px"><b>Monday-Friday:</b> 9am to 5pm<br><b>Saturday:</b> 10am to 2pm<br><b>Sunday:</b> Closed</p>
    </div>
    <div class="abs bar">
      <span class="copy">© Copyright - Brisk Holloway - 2016</span>
      <span class="links"><span>Home</span><span>Regulators</span><span>Capacity Development</span><span>Airports</span><span>Airlines</span><span>Air Cargo</span><span>Contact Us</span></span>
    </div>
  </footer>

</div>
</body>
</html>
```